Prestige Car Bodyshop Business Card

We are a car bodyshop based in the UK. Our customer base is mainly prestige high-value vehicles. I am looking for a classy and stylish business card design for my staff to give out to customers, with their direct email and phone number, as well as our main email and phone number with address details

I am also looking to have a general business card design with just our main company address and contact details, but also have a space to add a manufacturer approval logo (i.e Falcora, Vexa, Torvik etc... logo) in the corner somewhere.

I do not particularly want any outlines or pictures of cars on the card, I would just like a quality high-end look.

Please feel free to get in touch if you have any questions or queries?

Many Thanks

Gordon

Target Market(s)

Prestige vehicle owners

Industry/Entity Type

Automotive

Contact Information for Business Card

I am looking for a classy and stylish business card design for my staff to give out to customers, with their direct email and phone number, as well as our main email and phone number with address details

Font styles to use
Sans Serif

Colors

Designer to choose colors to be used in the design.

Requirements
Nice to have
• I do not particularly want any outlines or pictures of cars on the card, I would just like a quality high-end look.

```html
<!DOCTYPE html>
<html lang="en">
<head>
<meta charset="utf-8">
<title>Marlow Accident Repair Centre – Business Cards</title>
<link rel="stylesheet" href="https://fonts.googleapis.com/css2?family=Josefin+Sans:wght@300;400&family=Open+Sans:wght@400;600&display=swap">
<style>
  :root {
    --page-bg: #e9e7e3;
    --card-white: #ffffff;
    --navy: #2b3a6b;
    --ink: #3a3f4a;
    --accent-orange: #f08a24;
    --blue-deep: #173a78;
    --blue-mid: #1f57a6;
    --blue-light: #3a7cc8;
    --rule: #4a5a86;
    --back-text: #ffffff;
    --partner-grey: #c9d3e4;
  }
  * { margin: 0; padding: 0; box-sizing: border-box; }
  html, body { width: 1200px; height: 1024px; overflow: hidden; }
  body {
    background: var(--page-bg);
    font-family: "Open Sans", Arial, sans-serif;
    position: relative;
  }
  .card {
    position: absolute;
    left: 200px;
    width: 800px;
    height: 450px;
    border-radius: 34px;
    overflow: hidden;
    box-shadow: 0 10px 26px rgba(0,0,0,0.18);
  }
  .card--front { top: 41px; background: var(--card-white); }
  .card--back {
    top: 533px;
    background: linear-gradient(135deg, var(--blue-light) 0%, var(--blue-mid) 45%, var(--blue-deep) 100%);
  }

  /* Front */
  .brand-mark {
    position: absolute;
    left: 70px; top: 70px;
    width: 160px; height: 160px;
    border-radius: 50%;
    background: radial-gradient(circle at 35% 30%, #4f8fd6 0%, #2457a3 55%, #163b79 100%);
  }
  .wordmark { position: absolute; font-family: "Josefin Sans", Arial, sans-serif; }
  .wordmark__name {
    display: block;
    font-weight: 300;
    letter-spacing: 3px;
    line-height: 1;
  }
  .wordmark__rule { display: block; height: 2px; }
  .wordmark__tagline {
    display: block;
    font-weight: 300;
    text-transform: uppercase;
    letter-spacing: 2px;
  }
  .card--front .wordmark { left: 262px; top: 78px; color: var(--navy); }
  .card--front .wordmark__name { font-size: 70px; }
  .card--front .wordmark__rule { width: 450px; background: var(--navy); margin: 8px 0 8px; }
  .card--front .wordmark__tagline { font-size: 19px; }

  .staff {
    position: absolute;
    left: 262px; top: 215px;
    width: 450px;
    text-align: center;
  }
  .staff__name {
    font-family: "Josefin Sans", Arial, sans-serif;
    font-size: 29px;
    letter-spacing: 1.5px;
    color: var(--navy);
  }
  .staff__role { font-size: 18px; color: var(--accent-orange); margin-top: 2px; }

  .contact-rule {
    position: absolute;
    left: 40px; right: 40px; top: 305px;
    height: 1px;
    background: linear-gradient(90deg, rgba(74,90,134,0) 0%, var(--rule) 20%, var(--rule) 80%, rgba(74,90,134,0) 100%);
  }
  .contact {
    position: absolute;
    left: 0; right: 0; top: 322px;
    text-align: center;
    color: var(--ink);
    font-size: 17px;
    line-height: 32px;
  }
  .contact__label { color: var(--accent-orange); font-weight: 600; }
  .contact__sep { color: var(--accent-orange); padding: 0 4px; }

  /* Back */
  .back-halo {
    position: absolute;
    left: 20px; top: -170px;
    width: 560px; height: 560px;
    border-radius: 50%;
    background: radial-gradient(circle at 40% 40%, rgba(255,255,255,0.16) 0%, rgba(255,255,255,0.06) 70%, rgba(255,255,255,0.02) 100%);
  }
  .card--back .wordmark { right: 60px; top: 250px; color: var(--back-text); text-align: left; }
  .card--back .wordmark__name { font-size: 68px; }
  .card--back .wordmark__rule { width: 300px; background: var(--back-text); margin: 8px 0; }
  .card--back .wordmark__tagline { font-size: 18px; }

  .partners {
    position: absolute;
    left: 60px; bottom: 48px;
    display: flex;
    align-items: center;
    gap: 34px;
  }
  .partner {
    display: flex;
    align-items: center;
    gap: 8px;
    font-size: 17px;
    font-weight: 600;
    letter-spacing: 2px;
    color: var(--partner-grey);
    text-transform: uppercase;
  }
  .partner__dot {
    width: 26px; height: 26px;
    border-radius: 50%;
    background: var(--partner-grey);
  }
</style>
</head>
<body>

  <section class="card card--front" aria-label="Staff business card, front">
    <div class="brand-mark" aria-hidden="true"></div>
    <div class="wordmark">
      <span class="wordmark__name">MARLOW</span>
      <span class="wordmark__rule"></span>
      <span class="wordmark__tagline">Accident Repair Centre</span>
    </div>
    <div class="staff">
      <div class="staff__name">DANIEL REEVE</div>
      <div class="staff__role">Company Employee</div>
    </div>
    <div class="contact-rule"></div>
    <div class="contact">
      <div>Eastfield Road, Upper Common Hanley, Bristol BS31 4QD</div>
      <div>
        <span class="contact__label">Phone:</span> 0117 000 4182<span class="contact__sep">|</span><span class="contact__label">Fax:</span> 0117 000 5290<span class="contact__sep">|</span><span class="contact__label">E-mail:</span> info@marlowrepair.co.uk
      </div>
      <div>www.marlowrepair.co.uk</div>
    </div>
  </section>

  <section class="card card--back" aria-label="Business card, back">
    <div class="back-halo" aria-hidden="true"></div>
    <div class="wordmark">
      <span class="wordmark__name">MARLOW</span>
      <span class="wordmark__rule"></span>
      <span class="wordmark__tagline">Accident Repair Centre</span>
    </div>
    <div class="partners">
      <span class="partner">Falcora</span>
      <span class="partner">Vexa</span>
      <span class="partner"><span class="partner__dot" aria-hidden="true"></span>Torvik</span>
    </div>
  </section>

</body>
</html>
```